Redesign of business card for Birchline Mechanical

We are looking for a new design for our business cards for Birchline Mechanical. We are a plumbing & HVAC construction company, operating on the West Coast of Canada and USA. Logo attached.
Industry/Entity Type
Construction - Plumbing & HVAC
Contact Information for Business Card
Name, address, phone numbers, email, website address
Look and feel
Each slider illustrates characteristics of the customer's brand and the style your logo design should communicate.

```html
<!DOCTYPE html>
<html lang="en">
<head>
<meta charset="utf-8">
<title>Birchline Mechanical – Business Card</title>
<link rel="stylesheet" href="https://fonts.googleapis.com/css2?family=Arimo:wght@400;700&family=Roboto+Condensed:wght@700&display=swap">
<style>
  :root {
    --backdrop: #d8d8d8;
    --card-light: #fbfbfb;
    --card-dark: #2f2f2f;
    --ink: #111111;
    --ink-soft: #555555;
    --rule: #c9c9c9;
    --band-grey: #8a8a8a;
    --band-black: #0c0c0c;
    --mark-on-dark: #8c8c8c;
    --text-on-dark: #e6e6e6;
  }
  * { margin: 0; padding: 0; box-sizing: border-box; }
  html, body { width: 1200px; height: 1040px; overflow: hidden; }
  body { background: var(--backdrop); position: relative; font-family: "Arimo", Arial, sans-serif; color: var(--ink); }

  .card { position: absolute; width: 644px; height: 368px; border-radius: 16px; overflow: hidden; }
  .card--front { left: 286px; top: 130px; background: var(--card-light); }
  .card--back { left: 284px; top: 568px; background: var(--card-dark); }

  .brand { position: absolute; left: 70px; top: 140px; width: 190px; display: flex; align-items: center; gap: 10px; }
  .brand__square { width: 18px; height: 18px; background: var(--ink); flex: none; }
  .brand__name { font-size: 19px; font-weight: 700; line-height: 1.15; color: var(--ink); }

  .divider { position: absolute; left: 272px; top: 98px; width: 1px; height: 168px; background: var(--rule); }

  .details { position: absolute; left: 293px; top: 90px; }
  .details__name { font-family: "Roboto Condensed", "Arial Narrow", sans-serif; font-weight: 700; font-size: 26px; line-height: 1; }
  .details__title { font-size: 16px; color: var(--ink-soft); margin-top: 3px; }
  .details__address { font-size: 16px; line-height: 20px; margin-top: 14px; }
  .contact { list-style: none; margin-top: 12px; font-size: 16px; line-height: 20px; }
  .contact li { display: flex; align-items: center; gap: 9px; }
  .contact svg { width: 12px; height: 12px; fill: var(--ink); flex: none; }

  .band-line { position: absolute; left: 0; right: 0; top: 345px; height: 3px; background: var(--band-grey); }
  .band { position: absolute; left: 0; right: 0; top: 350px; height: 18px; background: var(--band-black); }

  .back-brand { position: absolute; left: 0; right: 0; top: 145px; text-align: center; font-size: 40px; font-weight: 700; color: var(--mark-on-dark); }
  .back-brand__square { display: inline-block; width: 30px; height: 30px; background: var(--mark-on-dark); vertical-align: -3px; margin-right: 14px; }
  .back-web { position: absolute; left: 0; right: 0; top: 324px; text-align: center; font-size: 16px; color: var(--text-on-dark); }
</style>
</head>
<body>
  <section class="card card--front">
    <div class="brand">
      <span class="brand__square"></span>
      <span class="brand__name">Birchline Mechanical</span>
    </div>
    <div class="divider"></div>
    <div class="details">
      <h1 class="details__name">Daniel Harper</h1>
      <p class="details__title">President</p>
      <p class="details__address">2170 Alder Crest Road<br>Lakemont, NY 11040</p>
      <ul class="contact">
        <li><svg viewBox="0 0 12 12" aria-hidden="true"><path d="M2.4 0.5l2 2.3-1.1 1.5c.7 1.6 2 2.9 3.6 3.6l1.5-1.1 2.3 2-1 2.1C5.2 10.7 1.3 6.8.4 1.5z"/></svg>(612) 5390-7718</li>
        <li><svg viewBox="0 0 12 12" aria-hidden="true"><path d="M0 2.5h12v1L6 7 0 3.5zM0 4.6l6 3.5 6-3.5V10H0z"/></svg>name@birchlinemechanical.com</li>
        <li><svg viewBox="0 0 12 12" aria-hidden="true"><circle cx="6" cy="6" r="5.5"/><path d="M3 3.5c1 .2 1.6 1 1.4 2-.3.8.6 1.3.6 2.3 0 .7.6 1.5 1.2 1.4M7.5 1.2c-.4.9.2 1.6 1 1.8.9.2 1.1 1.4 2.2 1.3" fill="none" stroke="#fbfbfb" stroke-width="1"/></svg>www.birchlinemechanical.com</li>
      </ul>
    </div>
    <div class="band-line"></div>
    <div class="band"></div>
  </section>

  <section class="card card--back">
    <div class="back-brand"><span class="back-brand__square"></span>Birchline Mechanical</div>
    <p class="back-web">www.birchlinemechanical.com</p>
  </section>
</body>
</html>
```